Surgery Office Letterhead Design

I'm seeking new letterhead that will comprise all of our office locations and logo and other applicable information, per the following:

Office Locations:

Lakemont Institute for Jaw & Face Surgery at Cleburne
347 Hazelpine Court
Cleburne, Texas 76033
Phone 817.382.4706
Fax 817.382.9034

Lakemont Institute for Jaw & Face Surgery at Stephenville
518 Willowgate Boulevard
Stephenville, Texas 76401
Phone 254.563.2781
Fax 254.563.2789

Lakemont Institute for Jaw & Face Surgery at Belton
739 West 9th Avenue
Belton, Texas 76513
Phone 254.871.4035
Fax 254.871.4042

Other Info to include:

www.lakemontjawface.com
hello@lakemontjawface.com

Industry/Entity Type

Medical

Font styles to use
Serif
Sans Serif

Requirements
Must have
• See Project Description

```html
<!DOCTYPE html>
<html lang="en">
<head>
<meta charset="utf-8">
<title>Lakemont Institute for Jaw &amp; Face Surgery – Letterhead</title>
<link href="https://fonts.googleapis.com/css2?family=Cinzel:wght@500&family=Open+Sans:wght@400&display=swap" rel="stylesheet">
<style>
  :root {
    --navy: #1f3a5f;
    --ink: #4a4f57;
    --paper: #ffffff;
    --watermark: #eef0f4;
    --band: #e6e6e6;
    --footer-text: #8d8f93;
  }
  html, body {
    margin: 0;
    padding: 0;
    overflow: hidden;
    background: var(--paper);
  }
  .letterhead {
    position: relative;
    width: 849px;
    height: 1200px;
    background: var(--paper);
    overflow: hidden;
  }
  .brand {
    position: absolute;
    left: 56px;
    top: 34px;
    color: var(--navy);
    font-family: "Cinzel", serif;
    font-weight: 500;
    line-height: 1;
  }
  .brand-name {
    display: block;
    font-size: 30px;
    letter-spacing: 0.5px;
  }
  .brand-tagline {
    display: block;
    font-size: 14.5px;
    margin-top: 6px;
    letter-spacing: 0.3px;
  }
  .offices {
    position: absolute;
    left: 684px;
    top: 16px;
    font-family: "Open Sans", sans-serif;
    font-size: 10px;
    color: var(--ink);
    line-height: 1.35;
  }
  .office + .office {
    margin-top: 9px;
  }
  .contact-row {
    display: flex;
    align-items: flex-start;
    gap: 8px;
    margin-bottom: 2px;
    white-space: nowrap;
  }
  .contact-row svg {
    flex: none;
    width: 10px;
    height: 11px;
    margin-top: 1px;
    fill: var(--navy);
  }
  .watermark {
    position: absolute;
    left: 300px;
    top: 380px;
    width: 260px;
    height: 260px;
    border-radius: 50%;
    background: var(--watermark);
  }
  .footer-band {
    position: absolute;
    left: 0;
    bottom: 0;
    width: 100%;
    height: 34px;
    background: var(--band);
    font-family: "Open Sans", sans-serif;
    font-size: 10px;
    letter-spacing: 3px;
    color: var(--footer-text);
  }
  .footer-web {
    position: absolute;
    left: 62px;
    top: 11px;
  }
  .footer-email {
    position: absolute;
    right: 40px;
    top: 11px;
    letter-spacing: 1.5px;
  }
</style>
</head>
<body>
<div class="letterhead">
  <div class="brand">
    <span class="brand-name">LAKEMONT INSTITUTE</span>
    <span class="brand-tagline">FOR JAW &amp; FACE SURGERY</span>
  </div>

  <div class="offices">
    <div class="office">
      <div class="contact-row">
        <svg viewBox="0 0 10 12" aria-hidden="true"><path d="M5 0a4 4 0 0 0-4 4c0 3 4 8 4 8s4-5 4-8a4 4 0 0 0-4-4zm0 5.6A1.6 1.6 0 1 1 5 2.4a1.6 1.6 0 0 1 0 3.2z"/></svg>
        <div>347 Hazelpine Court<br>Cleburne, Texas 76033</div>
      </div>
      <div class="contact-row">
        <svg viewBox="0 0 10 10" aria-hidden="true"><path d="M2 0.5l1.8 2.2-1 1.2c.6 1.3 1.6 2.3 2.9 2.9l1.2-1L9.5 7.6 8.3 9.5C4 9.2.8 6 .5 1.7z"/></svg>
        <div>Phone 817.382.4706</div>
      </div>
      <div class="contact-row">
        <svg viewBox="0 0 10 10" aria-hidden="true"><rect x="0.5" y="3" width="9" height="6" rx="1"/><rect x="2.5" y="0.5" width="5" height="3" fill="none" stroke="#1f3a5f" stroke-width="1"/></svg>
        <div>Fax 817.382.9034</div>
      </div>
    </div>

    <div class="office">
      <div class="contact-row">
        <svg viewBox="0 0 10 12" aria-hidden="true"><path d="M5 0a4 4 0 0 0-4 4c0 3 4 8 4 8s4-5 4-8a4 4 0 0 0-4-4zm0 5.6A1.6 1.6 0 1 1 5 2.4a1.6 1.6 0 0 1 0 3.2z"/></svg>
        <div>518 Willowgate Boulevard<br>Stephenville, Texas 76401</div>
      </div>
      <div class="contact-row">
        <svg viewBox="0 0 10 10" aria-hidden="true"><path d="M2 0.5l1.8 2.2-1 1.2c.6 1.3 1.6 2.3 2.9 2.9l1.2-1L9.5 7.6 8.3 9.5C4 9.2.8 6 .5 1.7z"/></svg>
        <div>Phone 254.563.2781</div>
      </div>
      <div class="contact-row">
        <svg viewBox="0 0 10 10" aria-hidden="true"><rect x="0.5" y="3" width="9" height="6" rx="1"/><rect x="2.5" y="0.5" width="5" height="3" fill="none" stroke="#1f3a5f" stroke-width="1"/></svg>
        <div>Fax 254.563.2789</div>
      </div>
    </div>

    <div class="office">
      <div class="contact-row">
        <svg viewBox="0 0 10 12" aria-hidden="true"><path d="M5 0a4 4 0 0 0-4 4c0 3 4 8 4 8s4-5 4-8a4 4 0 0 0-4-4zm0 5.6A1.6 1.6 0 1 1 5 2.4a1.6 1.6 0 0 1 0 3.2z"/></svg>
        <div>739 West 9th Avenue<br>Belton, Texas 76513</div>
      </div>
      <div class="contact-row">
        <svg viewBox="0 0 10 10" aria-hidden="true"><path d="M2 0.5l1.8 2.2-1 1.2c.6 1.3 1.6 2.3 2.9 2.9l1.2-1L9.5 7.6 8.3 9.5C4 9.2.8 6 .5 1.7z"/></svg>
        <div>Phone 254.871.4035</div>
      </div>
      <div class="contact-row">
        <svg viewBox="0 0 10 10" aria-hidden="true"><rect x="0.5" y="3" width="9" height="6" rx="1"/><rect x="2.5" y="0.5" width="5" height="3" fill="none" stroke="#1f3a5f" stroke-width="1"/></svg>
        <div>Fax 254.871.4042</div>
      </div>
    </div>
  </div>

  <div class="watermark" aria-hidden="true"></div>

  <div class="footer-band">
    <div class="footer-web">www.lakemontjawface.com</div>
    <div class="footer-email">hello@lakemontjawface.com</div>
  </div>
</div>
</body>
</html>
```